Torvel & Company: Business Cards, Stationery & Envelopes
Our Tagline is "Be Clear."
Simple
Marla Drosset
Founder, Torvel & Company
217 Meadow Lantern Dr.
Fernhollow, Ashmere 27584
2816 Halloway Brook, NE
Atlanta, Georgia 30361
Marla@TorvelAndCo.example
www.TorvelAndCo.example
My consulting firm helps CEOs and other high-level executives with high-stakes communications. Our materials must exude professionalism and a modern, fresh, crisp and clean feel. The business cards, stationery and envelopes should match the look and feel of the logo and website. I'm interested in seeing designs that incorporate our "Be Heard" tagline, as well as ones that don't.
I think I prefer a card that is single-sided, but if you think there's a cool design that puts some information such as our addresses on back, I'm open to it.
Here are the relevant logo files

```html
<!DOCTYPE html>
<html lang="en">
<head>
<meta charset="utf-8">
<title>Torvel &amp; Company – Business Card</title>
<link rel="stylesheet" href="https://fonts.googleapis.com/css2?family=Cinzel:wght@400;600&family=Crimson+Text:ital@0;1&display=swap">
<style>
  :root {
    --backdrop: #3b3b3d;
    --card: #ffffff;
    --red: #c8161d;
    --red-dark: #6e0a0e;
    --ink: #1c1c1c;
    --ink-soft: #4a4a4a;
    --rule: #c9c9c9;
  }
  * { box-sizing: border-box; margin: 0; padding: 0; }
  html, body {
    width: 1200px; height: 780px; overflow: hidden;
    background: var(--backdrop);
  }
  .business-card {
    position: absolute; left: 75px; top: 90px;
    width: 1050px; height: 600px;
    background: var(--card);
    border-radius: 6px;
    overflow: hidden;
    font-family: "Crimson Text", Georgia, serif;
    color: var(--ink);
  }
  .edge-bands { position: absolute; inset: 0; }
  .brand {
    position: absolute; left: 170px; top: 150px;
    display: flex; align-items: center; gap: 26px;
  }
  .brand-dot {
    width: 92px; height: 92px; border-radius: 50%;
    background: var(--red);
  }
  .brand-name {
    font-family: "Cinzel", "Times New Roman", serif;
    font-weight: 600; font-size: 54px; letter-spacing: 1px;
    color: var(--ink);
  }
  .brand-rule {
    position: absolute; left: 288px; top: 252px;
    width: 580px; height: 2px; background: var(--red);
  }
  .tagline {
    position: absolute; right: 182px; top: 258px;
    font-family: "Crimson Text", Georgia, serif;
    font-style: italic; font-size: 26px; color: var(--red);
  }
  .person {
    position: absolute; right: 525px; top: 322px;
    text-align: right;
  }
  .person-name {
    font-family: "Cinzel", "Times New Roman", serif;
    font-size: 34px; color: var(--red); line-height: 1.1;
  }
  .person-title {
    font-family: "Cinzel", "Times New Roman", serif;
    font-size: 20px; color: var(--ink); margin-top: 4px;
  }
  .address {
    position: absolute; right: 525px; top: 420px;
    text-align: right; font-size: 23px; line-height: 1.35;
    color: var(--ink-soft);
  }
  .divider {
    position: absolute; left: 547px; top: 322px;
    width: 1px; height: 170px; background: var(--rule);
  }
  .contact-list {
    position: absolute; left: 569px; top: 324px;
    list-style: none; font-size: 23px; color: var(--ink-soft);
  }
  .contact-list li {
    display: flex; align-items: center; gap: 10px;
    height: 40px;
  }
  .contact-icon { width: 20px; height: 20px; flex: none; }
</style>
</head>
<body>
  <article class="business-card">
    <svg class="edge-bands" width="1050" height="600" viewBox="0 0 1050 600" aria-hidden="true">
      <defs>
        <linearGradient id="band-red" x1="0" y1="0" x2="1" y2="0">
          <stop offset="0" stop-color="#6e0a0e"/>
          <stop offset="1" stop-color="#c8161d"/>
        </linearGradient>
        <linearGradient id="band-red-right" x1="1" y1="0" x2="0" y2="0">
          <stop offset="0" stop-color="#6e0a0e"/>
          <stop offset="1" stop-color="#c8161d"/>
        </linearGradient>
      </defs>
      <path d="M0,0 H110 Q40,300 110,600 H0 Z" fill="url(#band-red)"/>
      <path d="M110,0 Q40,300 110,600" fill="none" stroke="#111" stroke-width="9"/>
      <path d="M1050,0 H960 Q1030,300 960,600 H1050 Z" fill="url(#band-red-right)"/>
      <path d="M960,0 Q1030,300 960,600" fill="none" stroke="#111" stroke-width="9"/>
    </svg>

    <div class="brand">
      <span class="brand-dot"></span>
      <span class="brand-name">Torvel &amp; Company</span>
    </div>
    <div class="brand-rule"></div>
    <div class="tagline">Be Clear.</div>

    <div class="person">
      <div class="person-name">Marla Drosset</div>
      <div class="person-title">CEO &amp; Founder</div>
    </div>
    <div class="address">
      217 Meadow Lantern Dr.<br>
      Fernhollow, Ashmere 27584
    </div>

    <div class="divider"></div>

    <ul class="contact-list">
      <li>
        <svg class="contact-icon" viewBox="0 0 20 20" aria-hidden="true">
          <path d="M5 2 L8 6 L6.5 8 Q8 11.5 12 13.5 L14 12 L18 15 L16 18 Q7 17 2 5 Z" fill="#c8161d"/>
        </svg>
        555.201.0137
      </li>
      <li>
        <svg class="contact-icon" viewBox="0 0 20 20" aria-hidden="true">
          <circle cx="10" cy="10" r="3.5" fill="none" stroke="#c8161d" stroke-width="2"/>
          <path d="M13.5 7 V12 Q13.5 14 15.5 14 Q18 14 18 10 A8 8 0 1 0 13 17.5" fill="none" stroke="#c8161d" stroke-width="2"/>
        </svg>
        Marla@TorvelAndCo.example
      </li>
      <li>
        <svg class="contact-icon" viewBox="0 0 20 20" aria-hidden="true">
          <circle cx="10" cy="10" r="8" fill="none" stroke="#c8161d" stroke-width="1.8"/>
          <ellipse cx="10" cy="10" rx="3.5" ry="8" fill="none" stroke="#c8161d" stroke-width="1.5"/>
          <path d="M2 10 H18 M3.5 6 H16.5 M3.5 14 H16.5" stroke="#c8161d" stroke-width="1.3"/>
        </svg>
        www.TorvelAndCo.example
      </li>
    </ul>
  </article>
</body>
</html>
```